Website for Swedish wellness company "Heartmeadow"

We need a website for our Swedish wellness company. The name is "Heartmeadow" . The company is all about sustainablility for our body, soul and planet. We work with coaching, yoga, massage, healthy food, retreats(sports, excercise, sufing), healing and inspirational talks. We are convinced that personal sustainability and a strong spiritual connection to yourself will lead to planetary sustainability. Our customers are both companies and consumers from all over the world. The final design should be clean/simple and you should get a feeling of community, happiness, warmth, connection,, joy, spirituality but still a professional touch.Just got a logo from Pixel Forum and are very happy with it;-)
Updates

Sorry I was too enthusiastic posting this project. Of course I will give you some text as well för the different pages! I will see to that it is finished by friday so if you want to wait with your submissions please do! Best regards Maja

Target Market(s)

Businesses and consumers

Industry/Entity Type

Health And Wellness

Number of Pages Required

5+ page

Font styles to use
Sans Serif

Colors
33a6d7
00a990
b7a5cd

Requirements
Must have
• Idea about pages:
• I am not sure how many pages I get for the price, but 5 would be nice to start with.
• Not sure what write ups is;-)
• But title of the pages could be:
• Landing page
• About us
• Services
• Retreats
• Contact us
Nice to have
• A clean and professional website but with some heart and soul in it. Because we Would love colours that harmonize with our logo, but other ideas are welcome!

```html
<!DOCTYPE html>
<html lang="en">
<head>
<meta charset="utf-8">
<title>Heartmeadow Wellness Centre</title>
<link href="https://fonts.googleapis.com/css2?family=Montserrat:ital,wght@0,400;0,500;0,600;0,700;1,400&family=Libre+Caslon+Text:wght@400&family=Comfortaa:wght@400;500&display=swap" rel="stylesheet">
<style>
:root{
  --accent:#1fb0a2;
  --green:#00a990;
  --sky:#33a6d7;
  --lavender:#b7a5cd;
  --blue:#125f94;
  --blue-deep:#0d4a7a;
  --ink:#222;
  --muted:#777;
  --light:#999;
  --charcoal:#363a3d;
  --panel:#676b6e;
}
*{margin:0;padding:0;box-sizing:border-box}
html,body{width:1200px;height:4200px;overflow:hidden}
body{position:relative;font-family:'Montserrat',sans-serif;color:var(--ink);background:#fff}
.abs{position:absolute}
.center{text-align:center}

/* header */
.topbar{left:0;top:0;width:1200px;height:29px;background:linear-gradient(90deg,var(--green),var(--sky) 55%,var(--lavender))}
.brand-mark{left:569px;top:8px;width:62px;height:62px;border-radius:50%;background:#fff;border:3px solid var(--accent)}
.brand-name{left:0;top:90px;width:1200px;text-align:center;font-family:'Libre Caslon Text',serif;font-size:23px;color:var(--blue-deep);letter-spacing:1px}
.nav{left:0;top:124px;width:1200px;height:46px;background:var(--blue-deep)}
.nav a{position:absolute;top:15px;font-size:13px;color:#fff;text-decoration:none;text-transform:uppercase}
.nav a.active::after{content:"";position:absolute;left:0;right:0;bottom:-14px;height:4px;background:var(--accent)}

/* hero */
.hero{left:0;top:170px;width:1200px;height:577px;
  background:
   radial-gradient(ellipse 260px 180px at 230px 200px,rgba(60,38,28,.85),transparent 70%),
   radial-gradient(ellipse 330px 230px at 860px 240px,rgba(226,186,158,.9),transparent 70%),
   radial-gradient(ellipse 240px 200px at 1080px 330px,rgba(102,190,176,.85),transparent 70%),
   radial-gradient(ellipse 230px 120px at 140px 470px,rgba(240,236,230,.9),transparent 70%),
   radial-gradient(ellipse 120px 90px at 800px 500px,rgba(255,214,150,.75),transparent 70%),
   linear-gradient(100deg,#4c3226 0%,#9a745c 30%,#b99478 55%,#8c6a54 78%,#6d8f87 100%)}
.hero::after{content:"";position:absolute;inset:0;background:rgba(0,0,0,.18)}
.hero-welcome{top:352px;left:0;width:1200px;font-family:'Comfortaa',sans-serif;font-size:20px;color:#fff}
.hero-title{top:386px;left:0;width:1200px;font-family:'Libre Caslon Text',serif;font-size:58px;color:#7fd8cd}
.hero-sub{top:460px;left:0;width:1200px;font-family:'Comfortaa',sans-serif;font-size:23px;color:#fff}
.btn-navy{left:531px;top:510px;width:136px;height:41px;background:var(--blue-deep);border-radius:5px;color:#fff;font-size:14px;line-height:41px;text-align:center}

/* about */
.about-photo{left:87px;top:840px;width:316px;height:316px;border-radius:50%;
  background:radial-gradient(circle at 62% 55%,#f0d2bd 0 30%,transparent 55%),
   radial-gradient(circle at 30% 30%,#4a2f24 0 22%,transparent 45%),
   radial-gradient(circle at 25% 45%,#fbf6ee 0 10%,transparent 20%),
   linear-gradient(135deg,#d9b59c,#b58d74)}
.about-stones{left:392px;top:872px;width:150px;height:256px;border-radius:45% 45% 40% 40%;
  background:radial-gradient(ellipse 60px 40px at 70% 35%,#fff 0 30%,transparent 70%),
   linear-gradient(180deg,#cfe4b8 0%,#7fb14f 40%,#2a2a2a 66%,#0f0f0f 100%)}
.about-title{left:544px;top:808px;font-family:'Libre Caslon Text',serif;font-weight:400;font-size:38px;color:var(--ink)}
.about-sub{left:544px;top:864px;font-family:'Comfortaa',sans-serif;font-size:13px;color:var(--ink)}
.about-text{left:544px;top:920px;width:570px;font-size:13px;line-height:24px;color:#555}
.about-text p{margin-bottom:24px}
.btn-teal{left:544px;top:1117px;width:137px;height:37px;background:var(--accent);border-radius:4px;color:#fff;font-size:14px;line-height:37px;text-align:center}

/* bands */
.band{left:0;width:1200px;
  background:radial-gradient(ellipse 300px 260px at 25% 40%,rgba(51,166,215,.35),transparent 70%),
   radial-gradient(ellipse 280px 240px at 75% 60%,rgba(183,165,205,.22),transparent 70%),
   linear-gradient(90deg,var(--blue-deep) 0%,var(--blue) 50%,var(--blue-deep) 100%)}
.section-title{left:0;width:1200px;font-family:'Libre Caslon Text',serif;font-weight:400;font-size:44px;text-align:center}
.divider{left:488px;width:224px;height:24px}

.services{top:1268px;height:579px}
.svc{top:1430px;width:240px;text-align:center;color:#fff}
.svc-ring{width:152px;height:152px;margin:0 auto;border-radius:50%;background:#fff;border:4px solid var(--accent);display:flex;align-items:center;justify-content:center}
.svc h3{font-family:'Libre Caslon Text',serif;font-weight:400;font-size:19px;margin-top:20px;letter-spacing:.5px}
.svc p{font-size:12.5px;line-height:20px;margin:12px auto 0;width:206px}
.arrow{top:1506px;width:49px;height:106px;background:rgba(255,255,255,.35)}

/* news */
.news-big{left:88px;top:2047px;width:487px;height:238px;
  background:radial-gradient(ellipse 60px 90px at 340px 160px,#0b0f18 0 60%,transparent 62%),
   linear-gradient(180deg,#1c3152 0%,#5f82aa 38%,#c4d6e6 60%,#4b6686 70%,#1d2a40 100%)}
.date-box{background:var(--accent);color:#fff;font-weight:700;text-align:center}
.news-main-title{left:186px;top:2308px;font-size:15px;font-weight:600;color:#333}
.news-meta{font-size:11px;color:var(--muted)}
.card{left:601px;width:489px;height:137px;border:1px solid #eee;background:#fff}
.card-img{left:0;top:0;width:196px;height:137px}
.card .tag{font-size:11px;color:var(--lavender);font-weight:500}
.card h4{font-size:15px;font-weight:600;color:#333}

/* testimonials */
.testi{top:2466px;height:538px}
.frame-side{border-color:#0b1b33;border-style:solid}
.avatar{left:555px;top:2660px;width:76px;height:76px;border-radius:50%;background:radial-gradient(circle at 50% 60%,#c7876b 0 35%,#5a2a20 70%)}
.quote{left:240px;top:2752px;width:708px;font-size:14px;font-style:italic;line-height:24px;color:#fff;text-align:center}
.t-name{left:0;top:2849px;width:1188px;text-align:center;color:#fff;font-weight:700;font-size:16px}
.t-role{left:0;top:2875px;width:1188px;text-align:center;color:#fff;font-size:13px}

/* blogs */
.blog{top:3179px;width:340px;text-align:center}
.blog-pic{width:258px;height:258px;margin:0 auto;border-radius:50%;border:5px solid var(--accent)}
.blog .meta{font-size:13px;color:var(--light);margin-top:22px}
.blog h4{font-size:15px;font-weight:600;color:#333;margin-top:12px}
.blog p{font-size:13px;color:#888;line-height:21px;margin-top:12px}

/* contact */
.contact{left:0;top:3627px;width:1200px;height:510px;background:radial-gradient(ellipse 500px 300px at 60% 40%,#4a4f53,transparent 70%),var(--charcoal)}
.info{left:212px;top:3672px;width:259px;height:419px;background:#fff}
.form{left:471px;top:3672px;width:548px;height:419px;background:var(--panel)}
.git{left:155px;top:3819px;width:272px;height:127px;background:var(--accent);color:#fff;font-family:'Libre Caslon Text',serif;font-size:46px;line-height:52px;padding:12px 30px}
.info-text{font-size:13px;color:#444;line-height:17px}
.social{top:4014px;width:38px;height:38px;border-radius:50%;background:#111}
.lbl{font-size:13px;color:#fff}
.field{background:#fff;border:1px solid #ddd}
.send{left:859px;top:4025px;width:129px;height:45px;border:1px solid #ddd;color:#fff;font-size:14px;line-height:43px;text-align:center}

.footer{left:0;top:4137px;width:1200px;height:63px;background:var(--blue-deep);color:#fff;font-size:13px;line-height:63px;text-align:center}
</style>
</head>
<body>

<header>
  <div class="abs topbar"></div>
  <div class="abs brand-mark"></div>
  <div class="abs brand-name">HEARTMEADOW</div>
  <nav class="abs nav">
    <a class="active" style="left:103px">Home</a>
    <a style="left:218px">About Us</a>
    <a style="left:345px">Services</a>
    <a style="left:470px">Retreats</a>
    <a style="left:597px">News and Updates</a>
    <a style="left:786px">Corporate Wellness</a>
    <a style="left:1000px">Contact Us</a>
  </nav>
</header>

<section>
  <div class="abs hero" role="img" aria-label="Photo of a woman with a flower in her hair receiving a shoulder massage beside candles and towels"></div>
  <div class="abs hero-welcome center">Welcome to Still Harbor</div>
  <div class="abs hero-title center">Experience the</div>
  <div class="abs hero-sub center">secrets of relaxation</div>
  <div class="abs btn-navy">CALL US FREE</div>
</section>

<section>
  <div class="abs about-photo" role="img" aria-label="Round portrait photo of a woman with a white flower in her hair"></div>
  <div class="abs about-stones" role="img" aria-label="Photo of a white flower and green leaves on black spa stones"></div>
  <h2 class="abs about-title">Heartmeadow Wellness Centre</h2>
  <div class="abs about-sub">Hello! I'm Dummy Text Insert</div>
  <div class="abs about-text">
    <p>Positive behavioral supports is a behavior management system used to under-<br>stand what maintains an individual's challenging behavior.</p>
    <p>People's inappropriate behaviors are difficult to change because they are func-<br>tional. Positive behavioral supports is a behavior management system used to un-<br>derstand what maintains an individual's challenging behavior. People's inappropri-<br>ate behaviors are difficult to change because they are functional.</p>
  </div>
  <div class="abs btn-teal">CALL US FREE</div>
</section>

<section>
  <div class="abs band services" role="img" aria-label="Blue-tinted photo of a therapist working with a client"></div>
  <h2 class="abs section-title" style="top:1300px;color:#fff">Our services</h2>
  <svg class="abs divider" style="top:1377px" viewBox="0 0 224 24"><line x1="0" y1="12" x2="90" y2="12" stroke="#fff"/><line x1="134" y1="12" x2="224" y2="12" stroke="#fff"/><circle cx="112" cy="12" r="9" fill="none" stroke="#fff" stroke-width="2"/></svg>
  <div class="abs arrow" style="left:0"><svg width="49" height="106"><polyline points="30,40 18,53 30,66" fill="none" stroke="#fff" stroke-width="2"/></svg></div>
  <div class="abs arrow" style="left:1151px"><svg width="49" height="106"><polyline points="19,40 31,53 19,66" fill="none" stroke="#fff" stroke-width="2"/></svg></div>
  <div class="abs svc" style="left:98px"><div class="svc-ring" role="img" aria-label="Chiropractic treatment icon"><svg width="90" height="70" viewBox="0 0 90 70"><rect x="8" y="40" width="74" height="6" fill="var(--accent)"/><line x1="16" y1="46" x2="16" y2="62" stroke="var(--accent)" stroke-width="4"/><line x1="74" y1="46" x2="74" y2="62" stroke="var(--accent)" stroke-width="4"/></svg></div><h3>CHIROPRACTIC</h3><p>Lorem Ipsum is simply dummy text of the printing and typeset-ting industry. Lorem Ipsum has been the industry's</p></div>
  <div class="abs svc" style="left:358px"><div class="svc-ring" role="img" aria-label="Physiotherapy icon"><svg width="90" height="70" viewBox="0 0 90 70"><rect x="8" y="40" width="74" height="6" fill="var(--accent)"/><line x1="16" y1="46" x2="16" y2="62" stroke="var(--accent)" stroke-width="4"/><line x1="74" y1="46" x2="74" y2="62" stroke="var(--accent)" stroke-width="4"/></svg></div><h3>PHYSIOTHERAPY</h3><p>Lorem Ipsum is simply dummy text of the printing and typeset-ting industry. Lorem Ipsum has been the industry's</p></div>
  <div class="abs svc" style="left:615px"><div class="svc-ring" role="img" aria-label="Rehabilitation icon"><svg width="90" height="70" viewBox="0 0 90 70"><circle cx="52" cy="48" r="15" fill="none" stroke="var(--accent)" stroke-width="4"/><line x1="52" y1="33" x2="52" y2="63" stroke="var(--accent)" stroke-width="2"/><line x1="37" y1="48" x2="67" y2="48" stroke="var(--accent)" stroke-width="2"/></svg></div><h3>REHABILITATION</h3><p>Lorem Ipsum is simply dummy text of the printing and typeset-ting industry. Lorem Ipsum has been the industry's</p></div>
  <div class="abs svc" style="left:874px"><div class="svc-ring" role="img" aria-label="Massage therapy icon"><svg width="90" height="70" viewBox="0 0 90 70"><rect x="8" y="40" width="74" height="6" fill="var(--accent)"/><line x1="16" y1="46" x2="16" y2="62" stroke="var(--accent)" stroke-width="4"/><line x1="74" y1="46" x2="74" y2="62" stroke="var(--accent)" stroke-width="4"/></svg></div><h3>MASSAGE THERAPY</h3><p>Lorem Ipsum is simply dummy text of the printing and typeset-ting industry. Lorem Ipsum has been the industry's</p></div>
</section>

<section>
  <h2 class="abs section-title" style="top:1888px;color:#333">News &amp; Updates</h2>
  <svg class="abs divider" style="top:1964px" viewBox="0 0 224 24"><line x1="0" y1="12" x2="90" y2="12" stroke="#888"/><line x1="134" y1="12" x2="224" y2="12" stroke="#888"/><circle cx="112" cy="12" r="9" fill="none" stroke="var(--lavender)" stroke-width="2"/><circle cx="112" cy="12" r="4" fill="var(--accent)"/></svg>

  <div class="abs news-big" role="img" aria-label="Photo of a person meditating in silhouette by the sea under a cloudy sky"></div>
  <div class="abs date-box" style="left:112px;top:2313px;width:51px;height:41px;font-size:24px;line-height:41px">02</div>
  <div class="abs news-meta" style="left:112px;top:2362px;width:51px;letter-spacing:6px;border-bottom:1px dotted #888;padding-bottom:4px">JUN</div>
  <div class="abs news-main-title">5 HEALTHY HABITS I DO EVERYDAY</div>
  <div class="abs news-meta" style="left:186px;top:2334px">At Whole Table Nutrition, we teach the concept of Primary</div>
  <div class="abs news-meta" style="left:186px;top:2358px">Food which is everything that nourishes your life</div>

  <div class="abs card" style="top:2047px">
    <div class="abs card-img" role="img" aria-label="Photo of a woman doing a yoga pose on a beach" style="background:radial-gradient(ellipse 50px 30px at 110px 70px,#6a5a50,transparent 70%),linear-gradient(180deg,#d4e6ee 0%,#eedcc4 55%,#d9c29f 75%,#6fb8b0 100%)"></div>
    <div class="abs date-box" style="left:222px;top:3px;width:106px;height:38px;font-size:18px;line-height:38px;text-align:left;padding-left:16px">17 <span style="font-size:10px;font-weight:500;margin-left:20px;border-left:1px solid #fff;padding-left:12px">JUN</span></div>
    <div class="abs tag" style="left:345px;top:16px">#NUTRITION</div>
    <h4 class="abs" style="left:222px;top:54px">Glow Guides Packs Are Here!</h4>
    <div class="abs news-meta" style="left:222px;top:88px">At Whole Table Nutrition, we teach th...</div>
  </div>
  <div class="abs card" style="top:2210px">
    <div class="abs card-img" role="img" aria-label="Photo of a woman exercising on a mat" style="background:radial-gradient(ellipse 40px 22px at 120px 70px,#4fb8c2,transparent 70%),radial-gradient(ellipse 60px 30px at 60px 60px,#3a2f2a,transparent 70%),linear-gradient(135deg,#e2e5e9,#c2ccd3)"></div>
    <div class="abs date-box" style="left:222px;top:3px;width:106px;height:38px;font-size:18px;line-height:38px;text-align:left;padding-left:16px">15 <span style="font-size:10px;font-weight:500;margin-left:20px;border-left:1px solid #fff;padding-left:12px">JUN</span></div>
    <div class="abs tag" style="left:345px;top:16px">#WORKOUT</div>
    <h4 class="abs" style="left:222px;top:54px">5 Tips to Help Get Yourself Back to</h4>
    <div class="abs news-meta" style="left:222px;top:88px">At Whole Table Nutrition, we teach th...</div>
  </div>
</section>

<section>
  <div class="abs band testi" role="img" aria-label="Blue-tinted photo of a therapist treating a client"></div>
  <div class="abs frame-side" style="left:179px;top:2538px;width:830px;height:404px;border-width:0 4px 4px 4px"></div>
  <div class="abs" style="left:179px;top:2538px;width:226px;height:4px;background:#0b1b33"></div>
  <div class="abs" style="left:783px;top:2538px;width:226px;height:4px;background:#0b1b33"></div>
  <h2 class="abs section-title" style="top:2508px;color:#fff">Our Testimonials</h2>
  <svg class="abs divider" style="top:2583px;left:498px" viewBox="0 0 224 24"><line x1="0" y1="12" x2="90" y2="12" stroke="#fff"/><line x1="134" y1="12" x2="224" y2="12" stroke="#fff"/><circle cx="112" cy="12" r="9" fill="none" stroke="#fff" stroke-width="2"/></svg>
  <div class="abs avatar" role="img" aria-label="Round portrait photo of the client"></div>
  <p class="abs quote">Lorem Ipsum is simply dummy text of the printing and typesetting industry. Lorem Ipsum has<br>been the industry's standard dummy text ever since the 1500s, when an unknown printer took a<br>galley of type and scrambled it to make a type specimen book.</p>
  <div class="abs t-name">Elias Brandt</div>
  <div class="abs t-role">Brightpath Studio</div>
</section>

<section>
  <h2 class="abs section-title" style="top:3037px;color:#333">Our Blogs</h2>
  <svg class="abs divider" style="top:3105px" viewBox="0 0 224 24"><line x1="0" y1="12" x2="90" y2="12" stroke="#888"/><line x1="134" y1="12" x2="224" y2="12" stroke="#888"/><circle cx="112" cy="12" r="9" fill="none" stroke="var(--lavender)" stroke-width="2"/><circle cx="112" cy="12" r="4" fill="var(--accent)"/></svg>
  <article class="abs blog" style="left:91px"><div class="blog-pic" role="img" aria-label="Photo of rolled grey towels with pink frangipani flowers" style="background:radial-gradient(circle at 35% 75%,#f3a9bf 0 10%,transparent 22%),radial-gradient(circle at 70% 70%,#f3a9bf 0 9%,transparent 20%),linear-gradient(180deg,#8c7f86,#6a5e62 60%,#b39a9a)"></div><div class="meta">April 21, 2017 &nbsp;|&nbsp; 10 Comments</div><h4>Labour Day Weekend Hours</h4><p>Lorem Ipsum has been the industry's<br>standard dummy text ever since the 1500s,<br>when an unknown printer</p></article>
  <article class="abs blog" style="left:430px"><div class="blog-pic" role="img" aria-label="Photo of hands massaging a foot beside a white lily" style="background:radial-gradient(circle at 50% 80%,#fbf8ee 0 14%,transparent 28%),radial-gradient(ellipse 120px 60px at 50% 50%,#f0d8c2,transparent 70%),linear-gradient(160deg,#9ccc5c,#d7e9b0 50%,#7cb84a)"></div><div class="meta">April 21, 2017 &nbsp;|&nbsp; 10 Comments</div><h4>Think Well Program</h4><p>Lorem Ipsum has been the industry's<br>standard dummy text ever since the 1500s,<br>when an unknown printer</p></article>
  <article class="abs blog" style="left:769px"><div class="blog-pic" role="img" aria-label="Photo of stacked stones and starfish on sand" style="background:radial-gradient(ellipse 50px 80px at 62% 45%,#8f8c88,transparent 70%),radial-gradient(circle at 35% 60%,#e0a760 0 12%,transparent 24%),linear-gradient(180deg,#9cc8d2 0%,#e6d7ba 55%,#cdb88f 100%)"></div><div class="meta">April 21, 2017 &nbsp;|&nbsp; 10 Comments</div><h4>Labour Day Weekend Hours</h4><p>Lorem Ipsum has been the industry's<br>standard dummy text ever since the 1500s,<br>when an unknown printer</p></article>
</section>

<section>
  <div class="abs contact" role="img" aria-label="Dark photo background"></div>
  <div class="abs info"></div>
  <div class="abs form"></div>
  <svg class="abs" style="left:232px;top:3692px" width="18" height="18"><circle cx="9" cy="9" r="7" fill="none" stroke="var(--accent)" stroke-width="2"/><polyline points="9,5 9,9 12,11" fill="none" stroke="var(--accent)" stroke-width="1.5"/></svg>
  <div class="abs info-text" style="left:262px;top:3689px">Monday - Friday 7:30am - 8pm<br>Saturday 10am - 5pm<br>Sunday 10am - 5pm</div>
  <div class="abs" style="left:230px;top:3747px;width:225px;border-top:1px solid #ddd"></div>
  <svg class="abs" style="left:232px;top:3761px" width="16" height="16"><path d="M3 2 L6 2 L7 5 L5 6 Q7 10 10 11 L11 9 L14 10 L14 13 Q8 14 4 9 Q2 5 3 2Z" fill="var(--accent)"/></svg>
  <div class="abs info-text" style="left:262px;top:3758px"><b>Phone:</b><br>555-014-2290</div>
  <div class="abs git">GET IN<br>TOUCH</div>
  <div class="abs info-text" style="left:234px;top:3986px;font-weight:600">Follow Us On</div>
  <div class="abs social" style="left:229px"></div>
  <div class="abs social" style="left:281px"></div>
  <div class="abs social" style="left:332px"></div>
  <div class="abs social" style="left:384px"></div>

  <div class="abs lbl" style="left:492px;top:3708px">Name</div>
  <div class="abs lbl" style="left:750px;top:3702px">Email</div>
  <div class="abs field" style="left:492px;top:3733px;width:238px;height:37px"></div>
  <div class="abs field" style="left:750px;top:3733px;width:238px;height:37px"></div>
  <div class="abs lbl" style="left:494px;top:3795px">Message</div>
  <div class="abs field" style="left:492px;top:3819px;width:496px;height:153px"></div>
  <div class="abs field" style="left:494px;top:3989px;width:12px;height:12px"></div>
  <div class="abs lbl" style="left:519px;top:3987px">Check this box if you are interested in wholesale</div>
  <div class="abs send">GET IN TOUCH</div>
</section>

<footer class="abs footer">Copyright 2017 by Heartmeadow Wellness Centre. All Rights Reserved.</footer>

</body>
</html>
```